Wendlow Cellars -responsive, bootstrap website design

Looking to build a responsive service website.

Logo and pictures have been provided.

PLEASE REVIEW ATTACHED DESIGN STYLE GUIDES & CLIENT CREATIVE BRIEF FOR OUR REQUIREMENT. THANK YOU AND GOOD LUCK!

```html
<!DOCTYPE html>
<html lang="en">
<head>
<meta charset="utf-8">
<title>Wendlow Cellars</title>
<link rel="stylesheet" href="https://fonts.googleapis.com/css2?family=Cinzel:wght@400;600&family=Montserrat:wght@400;500;600&family=Oswald:wght@400&display=swap">
<style>
:root{
  --teal-light:#66c6d1;
  --teal-mid:#6fa9b3;
  --teal-dark:#3e9db2;
  --ink:#1b1d1d;
  --white:#ffffff;
  --cta:#e4532b;
  --footer-bg:#0c0c0c;
  --footer-text:#d8d8d8;
  --icon-bg:#9a9a9a;
  --sky-top:#8fb3c4;
  --sky-pink:#e3a0a3;
  --sky-pale:#c7c3c4;
  --vine-light:#86ab45;
  --vine-dark:#557c2c;
  --bottle-dark:#141416;
}
*{margin:0;padding:0;box-sizing:border-box}
html,body{width:1200px;height:815px;overflow:hidden;background:var(--footer-bg)}
.page{position:relative;width:1200px;height:815px;overflow:hidden;font-family:"Montserrat",sans-serif}

.site-header{position:absolute;left:0;top:0;width:1200px;height:161px;
  background:linear-gradient(100deg,var(--teal-light) 0%,var(--teal-mid) 50%,var(--teal-dark) 100%);
  border-bottom:1px solid rgba(255,255,255,.8)}
.brand{position:absolute;left:282px;top:7px;width:183px;height:139px;display:flex;align-items:center;justify-content:center;
  font-family:"Cinzel",serif;font-weight:600;font-size:22px;color:var(--ink);text-align:center;line-height:1.2}
.join-link{position:absolute;left:953px;top:44px;font-size:11px;font-weight:600;color:var(--white);text-decoration:none}
.main-nav{position:absolute;left:706px;top:95px;display:flex;align-items:center;font-family:"Cinzel",serif;font-size:16px;font-weight:600;color:var(--white)}
.main-nav a{color:var(--white);text-decoration:none}
.main-nav .sep{margin:0 10px;font-family:"Montserrat",sans-serif;font-weight:400;font-size:15px}

.hero{position:absolute;left:0;top:162px;width:1200px;height:569px;
  background:linear-gradient(180deg,var(--sky-top) 0%,var(--sky-pink) 20%,var(--sky-pale) 45%,var(--vine-light) 62%,var(--vine-dark) 100%)}
.bottle-photo{position:absolute;left:353px;top:24px;width:125px;height:507px;border-radius:14px;
  background:linear-gradient(180deg,#2a2a2e 0%,var(--bottle-dark) 100%)}
.headline{position:absolute;left:578px;top:62px;color:var(--ink)}
.headline .kicker{font-size:18px;font-weight:500;letter-spacing:.5px;margin-left:4px}
.headline .title{font-family:"Cinzel",serif;font-size:68px;font-weight:400;letter-spacing:3px;line-height:1;margin-top:4px}
.headline .place{font-size:14px;font-weight:500;letter-spacing:1px;margin:5px 0 0 12px}
.buy-btn{position:absolute;left:594px;top:210px;width:88px;height:40px;background:var(--cta);border-radius:3px;
  color:var(--white);font-family:"Oswald",sans-serif;font-size:18px;display:flex;align-items:center;justify-content:center;text-decoration:none}
.call{position:absolute;left:704px;top:206px;color:var(--ink);font-family:"Cinzel",serif}
.call .label{font-size:12px;margin-left:4px;line-height:1}
.call .number{font-size:36px;line-height:1}

.site-footer{position:absolute;left:0;top:731px;width:1200px;height:84px;background:var(--footer-bg);border-top:2px solid #e8e8e8}
.copyright{position:absolute;left:181px;top:22px;font-family:Arial,sans-serif;font-size:11px;color:var(--footer-text)}
.footer-links{position:absolute;left:369px;top:22px;font-family:Arial,sans-serif;font-size:11px;color:var(--footer-text)}
.footer-links a{color:var(--footer-text);text-decoration:none}
.footer-links .sep{margin:0 5px}
.social{position:absolute;left:988px;top:17px;display:flex;gap:8px}
.social span{display:block;width:24px;height:24px;background:var(--icon-bg)}
</style>
</head>
<body>
<div class="page">
  <header class="site-header">
    <div class="brand">Wendlow Cellars</div>
    <a class="join-link" href="#">Join the family</a>
    <nav class="main-nav">
      <a href="#">New</a><span class="sep">|</span>
      <a href="#">About</a><span class="sep">|</span>
      <a href="#">Wines</a><span class="sep">|</span>
      <a href="#">Store</a><span class="sep">|</span>
      <a href="#">New</a>
    </nav>
  </header>

  <section class="hero" role="img" aria-label="Photo of vineyard rows under a pink sunset sky">
    <div class="bottle-photo" role="img" aria-label="Photo of a red wine bottle seen from the back label"></div>
    <div class="headline">
      <div class="kicker">FINEST QUALITY</div>
      <div class="title">WINES</div>
      <div class="place">WALLA, WALLA, WASHINGTON</div>
    </div>
    <a class="buy-btn" href="#">BUY NOW</a>
    <div class="call">
      <div class="label">CALL</div>
      <div class="number">1 555 0142</div>
    </div>
  </section>

  <footer class="site-footer">
    <div class="copyright">Copyright 2014&nbsp; WendlowCellars</div>
    <div class="footer-links"><a href="#">About Us</a><span class="sep">|</span><a href="#">Contact Us</a><span class="sep">|</span><a href="#">Terms and Conditions</a></div>
    <div class="social"><span></span><span></span><span></span></div>
  </footer>
</div>
</body>
</html>
```